Wealth Education Business Needs Sharp Business Card Design

We need a business card design for a recently launched investor education business called Harbor Crest.

The final design should promote security, empowerment, self improvement and financial gain. The card will ideally promote the stature of the business.

For more information and colours please visit harborcrest.com.au

Target Market(s)

Corporate executives and high net worth individuals

Industry/Entity Type

Education

Contact Information for Business Card

Name
Position
Contact Address
Phone
Mobile
Email
Website

```html
<!DOCTYPE html>
<html lang="en">
<head>
<meta charset="utf-8">
<title>Harbor Crest – Business Cards</title>
<link rel="stylesheet" href="https://fonts.googleapis.com/css2?family=Cormorant+Garamond:wght@500;600;700&display=swap">
<style>
  :root {
    --teal: #1aa683;
    --sky: #35b6ec;
    --leaf: #36c24f;
    --ink: #222;
    --paper: #ffffff;
    --stage: #e9ecec;
    --night: #0c0c0c;
    --night-soft: #2a2a2a;
    --silver: #c9c9c9;
    --silver-dim: #8d8d8d;
    --serif: "Cormorant Garamond", Georgia, serif;
  }
  * { box-sizing: border-box; margin: 0; padding: 0; }
  html, body { width: 842px; height: 1200px; overflow: hidden; }
  body { background: var(--stage); position: relative; font-family: var(--serif); color: var(--ink); }

  .card { position: absolute; overflow: hidden; }
  .card--light { width: 560px; height: 336px; left: 141px; background: var(--paper); box-shadow: 0 6px 18px rgba(0,0,0,.18); }
  .card--front { top: 40px; }
  .card--back  { top: 410px; }

  .band { position: absolute; background: var(--teal); }
  .band--top    { left: 62px; top: 0; width: 436px; height: 46px; border-radius: 0 0 26px 26px; box-shadow: 0 4px 8px rgba(0,0,0,.15); }
  .band--bottom { left: 62px; bottom: 0; width: 436px; height: 46px; border-radius: 26px 26px 0 0; box-shadow: 0 -4px 8px rgba(0,0,0,.15); }
  .band--left   { left: 0; top: 62px; width: 46px; height: 226px; border-radius: 0 26px 26px 0; box-shadow: 4px 0 8px rgba(0,0,0,.15); }
  .band--right  { right: 0; top: 62px; width: 46px; height: 226px; border-radius: 26px 0 0 26px; box-shadow: -4px 0 8px rgba(0,0,0,.15); }

  .accent { position: absolute; }
  .accent--front { left: 0; bottom: 40px; width: 200px; height: 110px;
    background: linear-gradient(135deg, var(--sky), var(--teal) 55%, var(--leaf));
    clip-path: polygon(0 35%, 55% 0, 100% 45%, 45% 100%, 0 100%); opacity: .85; }
  .accent--back { right: 20px; top: 0; width: 200px; height: 130px;
    background: linear-gradient(225deg, var(--sky), var(--teal) 50%, var(--leaf));
    clip-path: polygon(20% 0, 100% 0, 100% 50%, 55% 100%, 0 60%); opacity: .85; }

  .brand { position: absolute; font-family: var(--serif); font-weight: 700; letter-spacing: .08em; text-transform: uppercase; white-space: nowrap; }
  .card--front .brand { left: 44px; top: 146px; font-size: 26px; color: var(--ink); }
  .card--back .brand { left: 0; right: 0; top: 140px; text-align: center; font-size: 44px; letter-spacing: .1em; color: var(--teal); }

  .person { position: absolute; right: 52px; top: 96px; text-align: right; color: var(--teal); }
  .person__name { font-size: 25px; font-weight: 600; }
  .person__cred { font-size: 15px; font-weight: 500; margin-top: 2px; }

  .contacts { position: absolute; left: 302px; top: 194px; font-size: 15px; line-height: 1.25; font-weight: 500; }
  .contact { display: flex; gap: 8px; margin-bottom: 14px; }
  .contact svg { flex: none; width: 14px; height: 20px; margin-top: 2px; }

  .address { position: absolute; left: 0; right: 0; bottom: 22px; text-align: center; font-size: 17px; font-weight: 500; }

  .card--dark { top: 790px; width: 392px; height: 246px; border-radius: 28px;
    background: radial-gradient(ellipse at 70% -20%, var(--night-soft), var(--night) 60%);
    box-shadow: 0 0 0 5px #3a3a3a, 0 8px 18px rgba(0,0,0,.35); color: var(--silver); }
  .card--dark-front { left: 22px; }
  .card--dark-back  { left: 428px; }
  .card--dark .divider { position: absolute; left: 182px; top: 24px; bottom: 24px; width: 1px; background: linear-gradient(transparent, #555, transparent); }
  .card--dark .person { left: 30px; right: auto; top: 44px; text-align: left; color: var(--silver-dim); }
  .card--dark .person__name { font-size: 18px; }
  .card--dark .person__cred { font-size: 10px; }
  .card--dark .contacts { left: 22px; top: 112px; font-size: 11px; color: var(--silver); }
  .card--dark .contact { gap: 6px; margin-bottom: 26px; }
  .card--dark .contact svg { width: 11px; height: 15px; }
  .card--dark .brand { color: var(--silver); }
  .card--dark-front .brand { left: 182px; right: 0; top: 108px; text-align: center; font-size: 21px; }
  .card--dark-back .brand { left: 0; right: 0; top: 104px; text-align: center; font-size: 32px; }
  .card--dark .address { font-size: 13px; bottom: 26px; color: var(--silver); }
</style>
</head>
<body>

<svg width="0" height="0" style="position:absolute">
  <defs>
    <symbol id="icon-phone" viewBox="0 0 14 20"><path d="M7 1a6 6 0 0 1 6 6c0 4.5-6 12-6 12S1 11.5 1 7a6 6 0 0 1 6-6z" fill="none" stroke="currentColor" stroke-width="1.6"/><path d="M5 4.5l1.2 1.6-.8.9a4 4 0 0 0 1.8 1.8l.9-.8 1.6 1.2-.8 1.1c-2.4-.3-4.5-2.4-4.8-4.8z" fill="currentColor"/></symbol>
    <symbol id="icon-mail" viewBox="0 0 14 20"><path d="M7 1a6 6 0 0 1 6 6c0 4.5-6 12-6 12S1 11.5 1 7a6 6 0 0 1 6-6z" fill="none" stroke="currentColor" stroke-width="1.6"/><rect x="4" y="5" width="6" height="4" fill="none" stroke="currentColor" stroke-width="1"/><path d="M4 5l3 2.4L10 5" fill="none" stroke="currentColor" stroke-width="1"/></symbol>
  </defs>
</svg>

<section class="card card--light card--front">
  <div class="band band--top"></div>
  <div class="band band--bottom"></div>
  <div class="accent accent--front" role="img" aria-label="Decorative diagonal stripes in blue and green"></div>
  <div class="brand">Harbor Crest</div>
  <div class="person">
    <div class="person__name">Daniel Marwood</div>
    <div class="person__cred">BEc Grad Dip Wealth Planning</div>
  </div>
  <div class="contacts">
    <div class="contact" style="color:var(--sky)"><svg><use href="#icon-phone"/></svg><span style="color:var(--ink)">1300 555 214<br>INT: +613 5550 1782</span></div>
    <div class="contact" style="color:var(--sky)"><svg><use href="#icon-mail"/></svg><span style="color:var(--ink)">www.harborcrest.com.au<br>support@harborcrest.com.au</span></div>
  </div>
</section>

<section class="card card--light card--back">
  <div class="band band--left"></div>
  <div class="band band--right"></div>
  <div class="accent accent--back" role="img" aria-label="Decorative diagonal stripes in green and blue"></div>
  <div class="brand">Harbor Crest</div>
  <div class="address">Level 2, 47 Calder Street, Northbank VIC 3006</div>
</section>

<section class="card card--dark card--dark-front">
  <div class="person">
    <div class="person__name">Daniel Marwood</div>
    <div class="person__cred">BEc Grad Dip Wealth Planning</div>
  </div>
  <div class="contacts">
    <div class="contact" style="color:var(--sky)"><svg><use href="#icon-phone"/></svg><span style="color:var(--silver)">1300 555 214<br>INT: +613 5550 1782</span></div>
    <div class="contact" style="color:var(--sky)"><svg><use href="#icon-mail"/></svg><span style="color:var(--silver)">www.harborcrest.com.au<br>support@harborcrest.com.au</span></div>
  </div>
  <div class="divider"></div>
  <div class="brand">Harbor Crest</div>
</section>

<section class="card card--dark card--dark-back">
  <div class="brand">Harbor Crest</div>
  <div class="address">Level 2, 47 Calder Street, Northbank VIC 3006</div>
</section>

</body>
</html>
```